What makes us Different Managed Communications Services Provider Flyer

We need a flyer to explain why we are different than other "managed IT services" company. Gives a brief description of our company and services that can entice clients and potential clients to setup a FREE consultation with us. This will become part of an ongoing marketing campaign that includes emails, leave behinds, brochures, and more

```html
<!DOCTYPE html>
<html lang="en">
<head>
<meta charset="utf-8">
<title>Managed Communications Services Flyer</title>
<link href="https://fonts.googleapis.com/css2?family=Oswald:wght@500;600&family=Poppins:wght@300;400;500;600;700&display=swap" rel="stylesheet">
<style>
  :root {
    --backdrop: #c9c9c9;
    --navy: #08142e;
    --navy-mid: #0c2a5c;
    --brand-blue: #0d55a3;
    --brand-deep: #0a4690;
    --cyan: #14b6ec;
    --cyan-light: #1fd0f2;
    --ink: #1b1b1b;
    --white: #ffffff;
  }
  * { box-sizing: border-box; margin: 0; padding: 0; }
  html, body { width: 1200px; height: 864px; overflow: hidden; background: var(--backdrop); }
  body { position: relative; font-family: "Poppins", sans-serif; color: var(--ink); }

  .page { position: absolute; top: 73px; width: 538px; height: 695px; background: var(--white); overflow: hidden; }
  .page--front { left: 38px; }
  .page--back { left: 614px; }

  .hero { position: absolute; left: 0; top: 0; width: 538px; background: radial-gradient(circle at 30% 40%, #0f2c5e 0%, var(--navy) 70%); overflow: hidden; }
  .page--front .hero { height: 303px; }
  .page--back .hero { height: 299px; }

  .hero-photo { position: absolute; }
  .page--front .hero-photo { left: 250px; top: 0; width: 288px; height: 303px;
    background: radial-gradient(circle at 35% 25%, rgba(120,190,255,.55) 0%, rgba(20,90,190,.45) 30%, rgba(8,20,46,0) 70%),
                linear-gradient(120deg, rgba(8,20,46,0) 0%, #0f3c86 55%, #0a1d45 100%); }
  .page--back .hero-photo { left: 0; top: 0; width: 538px; height: 299px;
    clip-path: polygon(240px 0, 538px 0, 538px 299px, 288px 299px, 342px 198px);
    background: radial-gradient(circle at 72% 52%, #3ad6ff 0%, #1769c9 22%, #0c2d66 55%, #081634 100%); }
  .hero-divider { position: absolute; left: 0; top: 0; }

  .hero-kicker { position: absolute; left: 43px; top: 40px; font-weight: 400; font-size: 26px; line-height: 27px; color: var(--white); }
  .hero-title { position: absolute; left: 43px; font-family: "Oswald", sans-serif; font-weight: 600; font-size: 54px; line-height: 56px; letter-spacing: -.5px; }
  .hero-title--white { top: 98px; color: var(--white); }
  .hero-title--cyan { top: 154px; background: linear-gradient(90deg, #1a78e0, var(--cyan-light)); -webkit-background-clip: text; background-clip: text; color: transparent; }
  .hero-tagline { position: absolute; left: 46px; top: 215px; padding-left: 14px; border-left: 4px solid var(--cyan); font-weight: 600; font-size: 17.5px; line-height: 21px; color: var(--white); }

  .body-copy { font-size: 7.8px; line-height: 9.6px; text-align: justify; }
  .body-copy b { font-weight: 600; }
  .intro { position: absolute; left: 43px; top: 322px; width: 451px; }

  .section-heading { position: absolute; font-weight: 700; font-size: 14px; line-height: 16px; color: var(--ink); }
  .section-heading span { display: block; color: var(--brand-blue); }
  .commitment-heading { left: 43px; top: 404px; }
  .commitment-copy { position: absolute; left: 43px; top: 449px; width: 206px; text-align: left; }

  .photo { position: absolute; }
  .photo--team { left: 283px; top: 402px; width: 211px; height: 168px; border: 2px solid var(--white); box-shadow: 0 1px 4px rgba(0,0,0,.35);
    background: linear-gradient(135deg, #cfdbe6 0%, #a9b8c6 40%, #d8a86a 80%, #e0c05a 100%); }

  .footer-brand { position: absolute; left: 40px; top: 609px; display: flex; align-items: center; gap: 6px; font-weight: 600; font-size: 11px; color: var(--navy); }
  .footer-brand i { width: 10px; height: 10px; background: var(--cyan); display: block; }
  .footer-call { position: absolute; left: 215px; top: 597px; font-weight: 600; font-size: 20px; line-height: 24px; color: var(--brand-blue); white-space: nowrap; }
  .footer-call strong { color: var(--ink); font-weight: 600; }
  .footer-band { position: absolute; left: 0; top: 634px; width: 538px; height: 61px; }
  .footer-url { position: absolute; left: 241px; top: 648px; width: 260px; font-weight: 600; font-size: 15.5px; line-height: 18px; color: var(--white); white-space: nowrap; }

  .mgmt-kicker { position: absolute; left: 38px; top: 40px; font-weight: 600; font-size: 14px; color: var(--white); }
  .mgmt-title { position: absolute; left: 37px; top: 55px; font-family: "Oswald", sans-serif; font-weight: 500; font-size: 33px; line-height: 44px; letter-spacing: -.3px; color: var(--cyan-light); }
  .mgmt-rule { position: absolute; left: 38px; top: 98px; width: 38px; height: 2px; background: var(--cyan); }
  .mgmt-copy { position: absolute; left: 38px; top: 113px; width: 206px; color: var(--white); text-align: left; }
  .mgmt-list { position: absolute; left: 38px; top: 162px; width: 225px; list-style: none; }
  .mgmt-list li { position: relative; padding-left: 12px; margin-bottom: 9.5px; font-size: 7.8px; line-height: 9.6px; color: var(--white); }
  .mgmt-list li b { color: var(--cyan-light); font-weight: 600; }
  .mgmt-list svg { position: absolute; left: 0; top: 1px; }

  .deliver-heading { left: 37px; top: 320px; font-size: 13px; }
  .deliver-copy { position: absolute; left: 38px; top: 360px; width: 255px; }
  .deliver-copy p + p { margin-top: 9px; }
  .photo--office { left: 39px; top: 488px; width: 118px; height: 82px; border-radius: 4px; background: linear-gradient(160deg, #eef2f6 0%, #c9d3dc 60%, #8d9aa8 100%); }
  .photo--hands { left: 173px; top: 488px; width: 118px; height: 82px; border-radius: 4px; background: radial-gradient(circle at 50% 50%, #c49470 0%, #6f5a4b 45%, #3b3d44 100%); }

  .legacy-card { position: absolute; left: 315px; top: 323px; width: 189px; height: 246px; border-radius: 8px; background: linear-gradient(180deg, var(--cyan) 0%, #1a8fe6 55%, #1566e0 100%); padding: 16px 16px 0 19px; }
  .legacy-card h3 { font-weight: 700; font-size: 13px; line-height: 17px; color: var(--navy); margin-bottom: 14px; }
  .legacy-card p { color: var(--white); }
  .legacy-card p + p { margin-top: 9px; }
</style>
</head>
<body>

<section class="page page--front">
  <header class="hero">
    <div class="hero-photo" role="img" aria-label="Businessman in a suit holding a tablet with a glowing network lightbulb above it"></div>
    <p class="hero-kicker">More Than<br>Just a</p>
    <h1 class="hero-title hero-title--white">MANAGED</h1>
    <h1 class="hero-title hero-title--cyan">IT PROVIDER</h1>
    <p class="hero-tagline">We are a<br>Communications<br>Services Provider</p>
  </header>

  <p class="intro body-copy">At our company, we are far more than your typical managed IT provider. Since our founding in <b>1983</b>, we have built a reputation based on trust, reliability, and unparalleled service. With <b>client relationships spanning 20 to 30 years</b>, we have demonstrated a level of commitment that few IT firms can match. What sets us apart is not just our technical expertise but the <b>deep, long-term partnerships</b> we cultivate with our clients—many of whom have stayed with us <b>without ever being locked into a contract.</b> That is a testament to the exceptional quality of our service and the trust we have earned over decades.</p>

  <h2 class="section-heading commitment-heading">A COMMITMENT<span>BEYOND CONTRACTS</span></h2>
  <p class="commitment-copy body-copy">Unlike many managed IT providers who rely on rigid contracts to retain clients, we believe that service excellence speaks for itself. The longevity of our client relationships is rooted in our ability to <b>anticipate needs, resolve challenges before they escalate, and proactively enhance network &amp; communication infrastructures.</b><br>Our <b>comprehensive checklists, questionnaires, policies, and procedures, attention to details ensure that every client receives a tailored, best-in-class experience from day one.</b></p>

  <div class="photo photo--team" role="img" aria-label="Team of colleagues gathered around a computer and tablet in a bright office"></div>

  <div class="footer-brand"><i></i>Northpoint Voice &amp; Data</div>
  <p class="footer-call">CALL US NOW: <strong>555-014-2270</strong></p>
  <svg class="footer-band" width="538" height="61" viewBox="0 0 538 61" aria-hidden="true">
    <polygon points="222,0 232,0 196,43 186,43" fill="#14b6ec"/>
    <polygon points="240,0 538,0 538,43 204,43" fill="#0d55a3"/>
    <rect x="0" y="43" width="538" height="18" fill="#0a4690"/>
  </svg>
  <p class="footer-url">www.northpointvoicedata.com</p>
</section>

<section class="page page--back">
  <header class="hero">
    <div class="hero-photo" role="img" aria-label="Hand touching a glowing blue digital interface with binary code"></div>
    <svg class="hero-divider" width="538" height="299" viewBox="0 0 538 299" aria-hidden="true">
      <polyline points="234,0 336,198 282,299" fill="none" stroke="#ffffff" stroke-width="5"/>
    </svg>
    <p class="mgmt-kicker">A HOLISTIC APPROACH TO</p>
    <h1 class="mgmt-title">IT MANAGEMENT</h1>
    <div class="mgmt-rule"></div>
    <p class="mgmt-copy body-copy">We don't just manage IT—we integrate ourselves into your business, ensuring that technology aligns with your strategic goals. Our services go beyond traditional break-fix support; we offer</p>
    <ul class="mgmt-list">
      <li><svg width="7" height="7" viewBox="0 0 10 10"><circle cx="5" cy="5" r="5" fill="#14b6ec"/><polyline points="2.6,5.2 4.4,7 7.5,3.4" fill="none" stroke="#08142e" stroke-width="1.4"/></svg><b>Strategic IT Roadmaps</b> customized to drive business growth.</li>
      <li><svg width="7" height="7" viewBox="0 0 10 10"><circle cx="5" cy="5" r="5" fill="#14b6ec"/><polyline points="2.6,5.2 4.4,7 7.5,3.4" fill="none" stroke="#08142e" stroke-width="1.4"/></svg><b>Proactive cybersecurity assessments</b> that help keep businesses secure.</li>
      <li><svg width="7" height="7" viewBox="0 0 10 10"><circle cx="5" cy="5" r="5" fill="#14b6ec"/><polyline points="2.6,5.2 4.4,7 7.5,3.4" fill="none" stroke="#08142e" stroke-width="1.4"/></svg><b>Comprehensive backup and disaster recovery solutions</b> that provide peace of mind.</li>
      <li><svg width="7" height="7" viewBox="0 0 10 10"><circle cx="5" cy="5" r="5" fill="#14b6ec"/><polyline points="2.6,5.2 4.4,7 7.5,3.4" fill="none" stroke="#08142e" stroke-width="1.4"/></svg><b>Industry-leading response times and dedicated support teams</b> focused on delivering an exceptional client experience.</li>
    </ul>
  </header>

  <h2 class="section-heading deliver-heading">OUR CLIENTS STAY BECAUSE<span>WE DELIVER</span></h2>
  <div class="deliver-copy body-copy">
    <p>For over 40 years, we have maintained a standard of excellence that <b>other companies simply cannot compare with.</b> Our team of experts consistently goes above and beyond, ensuring that clients not only <b>get the support they need but also receive the strategic guidance necessary to stay ahead in an ever-evolving digital landscape.</b></p>
    <p>Our <b>90-day performance review</b> process ensures that we continuously improve our service based on client feedback. This process allows us to <b>adapt, refine, and enhance our approach,</b> providing a truly personalized IT experience that aligns with business objectives.</p>
  </div>

  <div class="photo photo--office" role="img" aria-label="Overhead view of a team standing in a modern office"></div>
  <div class="photo photo--hands" role="img" aria-label="Team members stacking hands together in a circle"></div>

  <aside class="legacy-card">
    <h3>A LEGACY OF TRUST<br>&amp; RELIABILITY</h3>
    <p class="body-copy">The fact that many of our clients have remained with us for decades without a formal contract speaks volumes about the trust we have built. We don't lock in clients with paperwork—we keep them with results. That's the difference between a standard managed IT provider and an IT partner who genuinely cares.</p>
    <p class="body-copy">If you're looking for an IT provider that will treat your business as if it were their own, look no further. Our legacy of service, innovation, and commitment to our clients is what sets us apart from the rest.</p>
  </aside>

  <div class="footer-brand"><i></i>Northpoint Voice &amp; Data</div>
  <p class="footer-call">CALL US NOW: <strong>555-014-2270</strong></p>
  <svg class="footer-band" width="538" height="61" viewBox="0 0 538 61" aria-hidden="true">
    <polygon points="222,0 232,0 196,43 186,43" fill="#14b6ec"/>
    <polygon points="240,0 538,0 538,43 204,43" fill="#0d55a3"/>
    <rect x="0" y="43" width="538" height="18" fill="#0a4690"/>
  </svg>
  <p class="footer-url">www.northpointvoicedata.com</p>
</section>

</body>
</html>
```